Motor Oil Lubricant Package Labels

We are looking for a logo and label that we can put on our motor oil bottle 1 liter and 5 liter. The name of our motor oil is Corvanta. We want to design our flagship logo for CORVANTA MOTOR OILS and as well as the label that will go on the bottle. We have some drafts that we have come up with attached and would like to see more options. The concept of a timeless motor oil and the endless loop of lubricating oils incorporated in the design. We will have full synthetic motor oil, a synthetic blend motor, ATF III transmission fluid, TRZ-IV transmission fluid. hydraulic oils etc. Examples will be attached
Target Market(s)
Automotive Lubricants and Chemicals
Industry/Entity Type
Automotive
Logo Text
Corvanta Lubricants
Font styles to use
Other font styles liked:
- Let designer choose
Requirements
Must have
- The Corvanta sign incorporated in a very cool way to our name. Our brand needs to stick out
Nice to have
- Automotive lubricant related and colors red, white, and blue incorporated in the design
Should not have
- Images of individuals and or topics not related to automotive lubricants.

```html
<!DOCTYPE html>
<html lang="en">
<head>
<meta charset="utf-8">
<title>Corvanta Motor Oil – 5W-30 Label</title>
<link rel="stylesheet" href="https://fonts.googleapis.com/css2?family=Archivo+Black&family=Arimo:wght@700&display=swap">
<style>
  :root {
    --page-bg: #ffffff;
    --white: #ffffff;
    --red-bright: #ec1c24;
    --red-deep: #3a070c;
    --black: #050505;
    --graphite: #3a3a3a;
    --blue-bright: #12aeea;
    --blue-mid: #0b64b4;
    --blue-deep: #071c55;
    --navy: #050c3a;
    --silver-light: #f2f2f2;
    --silver-dark: #7d7d7d;
  }
  * { margin: 0; padding: 0; box-sizing: border-box; }
  html, body { width: 1200px; height: 1000px; overflow: hidden; background: var(--page-bg); }
  .canvas { position: relative; width: 1200px; height: 1000px; }
  .label { position: absolute; left: 347px; top: 108px; width: 510px; height: 782px; }
  .label-art { position: absolute; inset: 0; width: 510px; height: 782px; }
  .label-text {
    position: absolute; color: var(--white);
    font-family: "Arimo", Arial, sans-serif; font-weight: 700; line-height: 1;
    white-space: nowrap;
  }
  .origin { left: 0; width: 510px; top: 45px; text-align: center; font-size: 20px; }
  .brand-name {
    left: 0; width: 510px; top: 218px; text-align: center;
    font-family: "Archivo Black", Arial, sans-serif; font-weight: 400; font-size: 48px;
    letter-spacing: 0.3em; padding-left: 0.3em;
  }
  .brand-sub {
    left: 0; width: 510px; top: 273px; text-align: center;
    font-family: "Archivo Black", Arial, sans-serif; font-weight: 400; font-size: 18px;
    letter-spacing: 0.62em; padding-left: 0.62em;
  }
  .blend-type { right: 56px; top: 518px; font-size: 22px; letter-spacing: 0.02em; }
  .grade-prefix {
    left: 52px; top: 636px; font-family: "Archivo Black", Arial, sans-serif; font-weight: 400; font-size: 34px;
    transform: rotate(-90deg); transform-origin: left top;
  }
  .grade {
    left: 86px; top: 538px; font-family: "Archivo Black", Arial, sans-serif; font-weight: 400;
    font-size: 110px; letter-spacing: -0.01em;
  }
  .spec { right: 56px; top: 644px; font-size: 30px; letter-spacing: 0.04em; }
  .volume { left: 0; width: 510px; top: 726px; text-align: center; font-size: 19px; }
</style>
</head>
<body>
<main class="canvas">
  <section class="label" aria-label="Corvanta Motor Oil 5W-30 bottle label">
    <svg class="label-art" viewBox="0 0 510 782" aria-hidden="true">
      <defs>
        <linearGradient id="redPanel" x1="0" x2="1" y1="0" y2="0">
          <stop offset="0" stop-color="var(--red-deep)"/>
          <stop offset="0.5" stop-color="var(--red-bright)"/>
          <stop offset="1" stop-color="var(--red-deep)"/>
        </linearGradient>
        <radialGradient id="blackBand" cx="0.5" cy="0.45" r="0.6">
          <stop offset="0" stop-color="var(--graphite)"/>
          <stop offset="1" stop-color="var(--black)"/>
        </radialGradient>
        <linearGradient id="bluePanelH" x1="0" x2="1" y1="0" y2="0">
          <stop offset="0" stop-color="var(--blue-deep)"/>
          <stop offset="0.5" stop-color="var(--blue-bright)"/>
          <stop offset="1" stop-color="var(--blue-deep)"/>
        </linearGradient>
        <linearGradient id="blueShade" x1="0" x2="0" y1="0" y2="1">
          <stop offset="0.55" stop-color="var(--navy)" stop-opacity="0"/>
          <stop offset="1" stop-color="var(--navy)" stop-opacity="0.85"/>
        </linearGradient>
        <linearGradient id="silver" x1="0" x2="1" y1="0" y2="0">
          <stop offset="0" stop-color="var(--silver-dark)"/>
          <stop offset="0.5" stop-color="var(--silver-light)"/>
          <stop offset="1" stop-color="var(--silver-dark)"/>
        </linearGradient>
        <clipPath id="labelShape"><rect width="510" height="782" rx="52"/></clipPath>
      </defs>
      <g clip-path="url(#labelShape)">
        <rect class="panel-blue" width="510" height="782" fill="url(#bluePanelH)"/>
        <rect class="panel-blue-shade" width="510" height="782" fill="url(#blueShade)"/>
        <rect class="panel-red" width="510" height="200" fill="url(#redPanel)"/>
        <path class="band-black" d="M0,80 C120,80 170,195 255,195 C340,195 390,78 510,78 L510,412 C390,412 340,300 255,300 C170,300 120,412 0,412 Z" fill="url(#blackBand)"/>
        <path class="band-edge" d="M0,80 C120,80 170,195 255,195 C340,195 390,78 510,78" fill="none" stroke="url(#silver)" stroke-width="8"/>
        <path class="band-edge" d="M0,412 C120,412 170,300 255,300 C340,300 390,412 510,412" fill="none" stroke="url(#silver)" stroke-width="8"/>
        <circle class="cert-badge" cx="245" cy="409" r="56" fill="var(--black)"/>
        <circle class="cert-badge-ring" cx="245" cy="409" r="49" fill="none" stroke="var(--white)" stroke-width="2"/>
        <circle class="cert-badge-core" cx="245" cy="409" r="35" fill="var(--white)"/>
      </g>
      <rect class="label-frame" x="15" y="15" width="480" height="752" rx="38" fill="none" stroke="var(--white)" stroke-width="1.5"/>
    </svg>

    <p class="label-text origin">MADE IN USA</p>
    <h1 class="label-text brand-name">CORVANTA</h1>
    <p class="label-text brand-sub">MOTOR OIL</p>
    <p class="label-text blend-type">SYNTHETIC&nbsp; BLEND</p>
    <p class="label-text grade-prefix">SAE</p>
    <p class="label-text grade">5W-30</p>
    <p class="label-text spec">API&nbsp; SN</p>
    <p class="label-text volume">32 oz. (946ml)</p>
  </section>
</main>
</body>
</html>
```